Harbor Oncology Partners Patient Referral Card

We need a 3.75" wide by 8.25" long patient referral card that a physician will fill out to refer their patient to Harbor Oncology Partners. The front of the card will have our logo on top, followed by contact information, a map that shows the office location and then there will be descriptive text at the bottom. On the back side, there will be a headshot photo with a brief bio of Dr. Marcus Whitfield. The address for the office is: 4175 N. Larchmont, Puyallup, WA 98461. The office phone number is 253.400.7218 and the website address is: harboroncologyhub.com

Target Market(s)

Physicians and medical staff

Font styles to use
Serif

Colors
34a7d8
33b8a4
9bcb3c

Requirements
Must have
• A map of the office location and two text boxes for descriptive language about services, and a photo and bio of Dr. Marcus Whitfield
Nice to have
• Clean and distinct design that is eye catching
Should not have
• Flowery or bold colors that distract from the content and purpose of the card

```html
<!DOCTYPE html>
<html lang="en">
<head>
<meta charset="utf-8">
<title>Harbor Oncology Partners – Patient Referral Card</title>
<link rel="stylesheet" href="https://fonts.googleapis.com/css2?family=Source+Serif+4:wght@300;400;700&display=swap">
<style>
  :root{
    --green:#9bcb3c;
    --teal:#33b8a4;
    --blue:#34a7d8;
    --logo-teal:#2bb3c0;
    --panel:#f3f3f3;
    --ink:#2b2b2b;
    --white:#ffffff;
  }
  *{box-sizing:border-box;margin:0;padding:0}
  html,body{width:960px;height:1200px;overflow:hidden;background:var(--white)}
  body{position:relative;font-family:"Source Serif 4",Georgia,serif;font-weight:300;color:var(--ink)}
  .card{position:absolute;top:126px;width:432px;height:948px;overflow:hidden}
  .card--front{left:30px;background:var(--panel)}
  .card--back{left:494px;background:var(--white);border:1px solid #ececec}

  /* front */
  .brand{position:absolute;left:0;top:0;width:100%;height:207px;display:flex;flex-direction:column;align-items:center;justify-content:center;gap:24px}
  .brand__row{display:flex;align-items:center;gap:14px}
  .brand__dot{width:18px;height:18px;border-radius:50%;background:var(--teal)}
  .brand__name{font-size:29px;font-weight:400;color:var(--logo-teal);letter-spacing:1px;line-height:1.2;text-align:center}
  .brand__tagline{font-size:13px;font-weight:400;letter-spacing:7px;color:var(--ink)}
  .rule{position:absolute;left:0;width:100%;height:3px;background:var(--green)}
  .rule--top{top:207px}
  .rule--map{top:395px}
  .contact{position:absolute;left:0;top:222px;width:100%;text-align:center;color:var(--green);font-size:17px;line-height:21px;font-weight:300}
  .contact__address{margin-bottom:22px}
  .map{position:absolute;left:0;top:398px;width:100%;height:229px;background:linear-gradient(135deg,#ebebe8 0%,#e4e6e2 55%,#e9ecef 100%)}
  .about{position:absolute;left:0;top:627px;width:100%;height:321px;background:var(--green);color:var(--white);text-align:center;padding:16px 24px 0}
  .about__title{font-size:18px;font-weight:700;margin-bottom:18px}
  .about__text{font-size:15px;line-height:19.2px;font-weight:300}

  /* back */
  .portrait{position:absolute;left:0;top:0;width:174px;height:212px;background:linear-gradient(180deg,#d9dcdf 0%,#9a9a98 55%,#3a3d42 100%)}
  .bio{position:absolute;left:174px;top:0;width:258px;height:212px;background:var(--green);color:var(--white);padding:24px 12px 0 18px}
  .bio__name{font-size:16px;line-height:21px;font-weight:300;margin-bottom:17px}
  .bio__text{font-size:15px;line-height:19.2px;font-weight:300}
  .form{position:absolute;left:31px;top:0;width:369px;height:100%}
  .field-label{position:absolute;left:0;font-size:17px;font-weight:400;color:var(--ink)}
  .field-line{position:absolute;left:0;width:369px;height:1px;background:var(--green)}
</style>
</head>
<body>

<section class="card card--front">
  <header class="brand">
    <div class="brand__row">
      <span class="brand__dot"></span>
      <span class="brand__name">Harbor Oncology<br>Partners</span>
    </div>
    <div class="brand__tagline">RADIATION ONCOLOGY</div>
  </header>
  <div class="rule rule--top"></div>

  <div class="contact">
    <p class="contact__address">4175 N. Larchmont<br>Puyallup, Pierce County 98461<br>USA</p>
    <p>care@harboroncologyhub.com<br>253-400-7218<br>253-400-7219</p>
  </div>
  <div class="rule rule--map"></div>

  <div class="map" role="img" aria-label="Street map showing the office location at 4175 N. Larchmont, Puyallup"></div>

  <div class="about">
    <h2 class="about__title">Exceeding Expectations One Patient at a Time</h2>
    <p class="about__text">Harbor Oncology Partners has been serving patients in the South Puget Sound Region with offices located in Puyallup, Washington. . Our Cancer Treatment Center is made up of highly skilled medical professionals who deeply value your health and wellbeing. We take great pride in providing our community with high quality, patient-centric care and health education. Proactive and preventative measures help keep our community healthier, and we work with that idea in mind. Harbor Oncology Partners has the wellness services you’d like when you’re feeling fine, and the emergency services you need when illness or injury strikes. Come in for a check-up.</p>
  </div>
</section>

<section class="card card--back">
  <div class="portrait" role="img" aria-label="Headshot photo of Dr. Marcus Whitfield"></div>
  <div class="bio">
    <p class="bio__name">Marcus Whitfield, MD PhD<br>Radiation Oncology</p>
    <p class="bio__text">The leading cancer care treatment center in the South Puget Sound Region of Washington State.&nbsp; We customize a treatment plan for your unique diagnosis.</p>
  </div>

  <div class="form">
    <span class="field-label" style="top:244px">Patient’s Name</span>
    <span class="field-line" style="top:276px"></span>

    <span class="field-label" style="top:333px">Description</span>
    <span class="field-line" style="top:364px"></span>
    <span class="field-line" style="top:405px"></span>
    <span class="field-line" style="top:446px"></span>
    <span class="field-line" style="top:486px"></span>
    <span class="field-line" style="top:527px"></span>
    <span class="field-line" style="top:568px"></span>
    <span class="field-line" style="top:609px"></span>
    <span class="field-line" style="top:650px"></span>
    <span class="field-line" style="top:690px"></span>
    <span class="field-line" style="top:731px"></span>
    <span class="field-line" style="top:772px"></span>

    <span class="field-label" style="top:876px">Referred by:</span>
    <span class="field-line" style="top:908px"></span>
  </div>
</section>

</body>
</html>
```